Mobile Repair Service on location needs a Web Design

We are starting a new mobile device repair service called Gadget Haven and our website needs a design!

Hello Designers!
First, we'd like to make clear this is more than a simple web design contest, we want the designers to create an idea. We want someone who can create the whole theme of the service's we provide. We want someone that can help design our visual branding, help us communicate a sentiment. And we are willing to pay for that.

Who are we?
Our company is based in Rotterdam, the Netherlands. We provide different services for all kinds of electronic devices. The kind of services we provide are, among other things, installations of hardware and software and the repair of broken or malfunctioning devices.
We are starting a new service that offers mobile device repairs on location, be it at the home of our customers, their office, or any other place. Just give us the address and we will come to you for the repair job. This is also our main USP. We have multiple skilled engineers who drive trough the country on a daily basis and can be on location within a working day. Repair is done immediately onsite while the customer waits. At this stage we will start with the smartphone product-group within the mobile devices. In a second phase we might also add tablets.
People don't want to be without their phone for weeks because of some parts that needed to be ordered by a repair center they had to sent their phone to. We offer a fully functional mobile repair center in the form of specially customized vans. These vans have all the tools and utilities needed by our engineers to safely repair your mobile device. Your phone is being repaired directly in front of you, the next business-day, on a location you desire.

For this new service we are creating a website called Gadget Haven. The website needs a story and matching design and this is where you come in. We are not looking for a simple template design we can get from any place. We need a story. We want you to create an idea, build a unique theme or vision that helps sell the product/service. This goes beyond the design of the website. We need the whole package, the design you are creating needs to have returning elements like icons, color use, images, maybe even characters etc. You name it! There needs to be a common thread in the design so we can reuse elements in, for example, the email templates, the work order or receipt we give to our customers (we may contact the winner of the contest to design these for us as well!).

The name 'Gadget Haven' is chosen. Haven (short for rehabilitate) has a bold and playful tone to it and the design needs to reflect the name. So we're looking for a somewhat playful and cheeky design. Definitely not too serious and definitely modern. We already got a logo that we love and that fit's this description (see attached design documents for the logo). It's bold, powerful and fun. Our web design needs to reflect this as well and has to fit in with our logo.
We would really like it if the design somehow incorporates elements that highlight our unique selling points (repairs on location, we come to you etc.). We would really like some form of story telling in the design. Think clumsy people breaking their phones. Teenagers in tears because they have no access to their friends. People nowadays have the need to always be 'connected'. What happens when your phone is broken or malfunctioning? We're handling tech, we are nerds and a little bit weird, but we're professionals and here to help you with your problem. The sentiment Wire Troop tries to communicate is something we really like. We're looking for fresh idea's, anything goes!

In an overview all Unique Selling Points of the Gadget haven service:
- Professional service on location. Don’t ship to us we will come to you!
- Clear pricing upfront. No hidden cost.
- Next business-day repair.
- Backed by a professional call center open 12 hours a day and open on a Saturday as well
- Backed by a professional repair center with more then 12 years of experience
- Repair is done by certified engineers
- 1 year warranty on the repair

The process:
The main function of our website will be for customers to make a repair request. A customer will visit our website and can make a repair request immediately by going through a 'request-order-flow'. In this flow he or she will need to fill in some forms and can select wich type/model/brand of mobile device he or she has and what parts need to be repaired. After a request is placed we will call the customer back (within an hour) for a short intake and to set a date/time and location. Our engineer will meet the customer at the specified location and will repair the device onsite in one of our mobile repair centers, which is a specialized van equipped with all the tools needed for device restorations.
So in short the steps are:
- Choose your device and repair job
- Place the order
- Get a callback within the hour
- Set date and location
- We will come to you.

Website functionality:
Our website is our main form of communication. So the sentiment we want to communicate needs be reflected in the design. We need a main/front page designed (preferably a long scrolling page design) containing:
1. Customers will be able to request a repair job directly on our website. So there will need to be a prominent button/link at the top of our main page that will bring the customer to this 'request-order-flow'. This is the main flow which needs to be full focus on the front page. All other items are secondary.
2. The general information of who we are and what we do, and why the customer should choose us. Preferably in short bullet-point type keywords/sentences with icons or other visual cues. See our unique selling points to get an idea of the information that will be displayed here.
3. There needs to be a section that will explain the process (see above) of a repair request step-by- step, again in brief short key sentences and with (custom) icons.
4. There needs to be a section that explains to the customer he/she can always contact us if they are not sure what the problem is with their device, and for this reason are not sure what repair request they should order.
5. We want to implement some functionality that display customer ratings or customer reviews. So there needs to be room for some kind of widget of plugin we're going to implement which shows these reviews.
6. A 'For business section' where we will explain all the options we provide for corporate clients.
7. Social media links.
8. There needs to be a menu with buttons that leads to the all sections described in the previous points.

For now, we need a design for our front page. In the second phase, when we have picked our winner, we may ask the winner to design the page(s) for our request workflow as well.

EDIT:
Finally, we have a very specific order in mind for the different segments of our website. We would like you to add some more segments that were not in our original brief as well:

1. Top header with order/request button. (should instantly make clear our main USP, we do repairs on location)
2. Our process
3. Our unique selling points / why choose us
4. The kind of repairs we do (broken screens, broken batteries, water damage, broken camera's, no sound etc.)
5. A 'meet our team' section, where we introduce some of our engineers
6. A 'contact us for any questions' section/
7. Testimonials/user reviews
8. A section where we show key performance indicators
9. 'For businesses' sections
10.'Subscribe for newsletter' field
11. Social media buttons

Industry/Entity Type

It Service

Number of Pages Required

1 page

Font styles to use
Sans Serif

Requirements
Must have
• a main/front page, design only
• custom icons/images for banners, adverts online and in print (high res)
Nice to have
• Storytelling in our design.
• Design that fits with our brand new logo.
• Elements like icons to have a flat design.
• Keep in mind that the website will need to be responsive when designing! (Ideally provide an example of the mobile design as well)
• Create a fun and trustworthy feeling.

```html
<!DOCTYPE html>
<html lang="en">
<head>
<meta charset="utf-8">
<title>Gadget Haven – Mobile Repair On Location</title>
<link href="https://fonts.googleapis.com/css2?family=Oswald:wght@400;500;700&family=Open+Sans:wght@400;600;700&display=swap" rel="stylesheet">
<style>
:root{
  --orange:#f26522;
  --orange-dark:#d9531a;
  --ink:#2b2b2b;
  --text:#555;
  --muted:#888;
  --light:#f2f2f2;
  --grey-band:#e6e6e6;
  --dark:#333436;
  --footer:#3a3a3b;
  --sky:#8db4cf;
  --white:#fff;
}
*{margin:0;padding:0;box-sizing:border-box}
html,body{width:1200px;height:3982px;overflow:hidden}
body{font-family:"Open Sans",Arial,sans-serif;color:var(--text);background:var(--white);font-size:13px;line-height:1.6}
section,header,footer{position:relative;width:1200px;overflow:hidden}
.heading{font-family:"Oswald",Arial,sans-serif;font-weight:500;color:var(--ink);text-transform:uppercase;font-size:22px;letter-spacing:.3px}
.rule{display:block;width:40px;height:3px;background:var(--orange);margin-top:10px}
.center{text-align:center}
.btn{display:inline-block;background:var(--orange);color:#fff;font-family:"Oswald",Arial,sans-serif;text-transform:uppercase;font-size:14px;letter-spacing:.5px;border-radius:3px;padding:9px 20px}
.brand{display:flex;align-items:center;gap:12px;font-family:"Oswald",Arial,sans-serif;font-weight:700;font-size:24px;line-height:1;color:#fff;text-transform:uppercase}
.brand-dot{width:44px;height:44px;border-radius:50%;background:var(--orange)}

/* HERO */
.hero{height:590px;background:linear-gradient(115deg,#2a2d31 0%,#4b4f55 40%,#6e6a66 70%,#3b3c3f 100%)}
.hero-photo{position:absolute;inset:0}
.nav{position:absolute;top:18px;left:172px;right:172px;display:flex;align-items:center;justify-content:space-between}
.nav-links{display:flex;align-items:center;gap:28px;font-family:"Oswald",Arial,sans-serif;font-size:14px;color:#fff;text-transform:uppercase}
.nav-links .btn{padding:8px 18px;margin-left:10px}
.hero-copy{position:absolute;left:172px;top:172px;color:#fff;font-family:"Oswald",Arial,sans-serif;text-transform:uppercase}
.hero-copy .line1{font-size:38px;letter-spacing:4px;font-weight:400}
.hero-copy .line2{font-size:62px;font-weight:700;line-height:1;letter-spacing:1px}
.hero-copy .tag{display:inline-block;background:var(--orange);font-size:26px;padding:2px 16px;margin-top:6px;letter-spacing:.5px}
.dots{position:absolute;bottom:44px;left:0;right:0;display:flex;justify-content:center;gap:8px}
.dots i{width:11px;height:11px;border-radius:50%;background:rgba(255,255,255,.55)}
.dots i.on{background:#fff;box-shadow:0 0 0 2px var(--orange)}

/* ABOUT */
.about{height:756px}
.about-col{position:absolute;top:42px;width:410px}
.about-col.left{left:172px}
.about-col.right{left:610px}
.about-col p{margin-top:24px;font-size:12.5px;line-height:1.65}
.about-col p+p{margin-top:18px}
.ticks{list-style:none;margin-top:18px}
.ticks li{display:flex;align-items:center;gap:10px;font-size:12.5px;margin-bottom:8px}
.ticks svg{flex:none}
.collage{position:absolute;left:172px;top:380px;width:380px;height:320px;background:linear-gradient(135deg,#7c8a8f,#b7a99a 50%,#5d676c)}
.van{position:absolute;left:560px;top:420px;width:470px;height:270px;background:linear-gradient(180deg,#f7f7f7,#dcdcdc);border-radius:40px 60px 18px 18px}

/* WHY */
.why{height:624px;background:var(--grey-band)}
.why .heading{padding-top:62px}
.why-lead{position:absolute;left:460px;width:280px;top:126px;text-align:center;font-size:12px;font-weight:600;color:var(--ink);line-height:1.4}
.ring{position:absolute;left:440px;top:193px;width:320px;height:320px;border-radius:50%;border:3px solid var(--orange)}
.ring-photo{position:absolute;left:500px;top:240px;width:200px;height:250px;border-radius:100px 100px 0 0;background:linear-gradient(180deg,#cfd6de,#2f4f8a 70%)}
.ring-icon{position:absolute;width:64px;height:64px;border-radius:50%;background:var(--orange);border:3px solid #fff;display:flex;align-items:center;justify-content:center}
.usp{position:absolute;width:220px;font-size:12px;font-weight:600;color:var(--ink);line-height:1.4}
.usp.l{text-align:right}

/* PROCESS */
.process{height:313px}
.process .heading{padding-top:60px}
.steps{position:absolute;top:140px;left:180px;right:180px;display:flex;justify-content:space-between}
.step{width:130px;text-align:center;position:relative}
.step-icon{width:96px;height:96px;margin:0 auto;border-radius:50%;border:3px solid #ddd;display:flex;align-items:center;justify-content:center}
.step p{margin-top:12px;font-size:12px;font-weight:600;color:var(--ink);line-height:1.35}
.step-arrow{position:absolute;right:-38px;top:40px}

/* REQUEST */
.request{height:285px;background:var(--sky)}
.request-notch{position:absolute;top:0;left:0}
.request-art{position:absolute;left:0;top:40px;width:340px;height:230px;background:linear-gradient(135deg,#6f9bb8,#a9c6da);opacity:.8}
.request .heading{position:absolute;top:78px;left:0;right:0;text-align:center;font-size:26px}
.form-row{position:absolute;top:142px;left:200px;display:flex;align-items:center;gap:12px}
.field{height:38px;background:#fff;border-radius:2px;font-size:12px;color:var(--muted);padding:0 12px;display:flex;align-items:center;justify-content:space-between}
.field.wide{width:335px}
.field.sel{width:205px;color:var(--ink)}
.radio{display:flex;align-items:center;gap:5px;font-size:12px;color:var(--ink);margin-left:6px}
.radio i{width:14px;height:14px;border-radius:50%;border:2px solid var(--ink);background:#fff}
.radio i.on{background:radial-gradient(circle,var(--ink) 40%,#fff 45%)}
.request .btn{position:absolute;top:208px;left:502px;width:196px;text-align:center}

/* REVIEWS */
.reviews{height:560px;background:linear-gradient(135deg,#2c2d2f,#4a4b4e 50%,#2e2f31)}
.reviews-stripe{position:absolute;top:0;left:0}
.reviews .quote{position:absolute;top:38px;left:0;right:0;text-align:center;font-family:Georgia,serif;font-size:52px;color:#fff;line-height:1}
.reviews .heading{position:absolute;top:80px;left:0;right:0;color:#fff;text-align:center}
.review{position:absolute;top:170px;width:265px;height:215px;background:#fff;border-radius:4px;padding:18px 20px 14px;text-align:center;font-size:11px;line-height:1.55;color:#777}
.stars{color:var(--orange);font-size:14px;letter-spacing:2px;margin-top:8px}
.review b{display:block;color:var(--ink);font-size:12px}
.review small{display:block;font-size:11px}
.avatar{position:absolute;top:410px;width:70px;height:70px;border-radius:50%;background:linear-gradient(180deg,#d9c7b8,#7b6a5f);border:4px solid #fff}
.avatar-line{position:absolute;top:385px;width:2px;height:25px;background:#fff}

/* CORPORATE */
.corporate{height:589px}
.corporate .heading{padding-top:70px}
.corp-card{position:absolute;top:142px;width:270px}
.corp-img{height:186px}
.corp-card h3{font-family:"Open Sans",Arial,sans-serif;font-size:14px;font-weight:700;color:var(--ink);line-height:1.3;margin-top:16px}
.corp-card .rule{width:36px;height:2px;margin-top:8px}
.corp-card p{font-size:11.5px;color:var(--muted);margin-top:10px;line-height:1.5}
.corp-card .btn{font-size:11px;padding:4px 9px;margin-top:14px;border-radius:2px}

/* FOOTER */
.footer{height:265px;background:var(--footer);color:#ddd}
.footer-tab{position:absolute;top:-1px;left:550px}
.footer .brand{position:absolute;left:172px;top:50px;font-size:28px}
.footer .brand-dot{width:56px;height:56px}
.footer .btn{position:absolute;left:172px;top:143px;font-size:13px;border-radius:16px;padding:7px 18px}
.copy{position:absolute;left:172px;top:195px;font-size:11px;color:#bbb}
.fcol{position:absolute;top:46px;font-size:12px;line-height:1.55;color:#ddd}
.fcol h4{font-family:"Oswald",Arial,sans-serif;font-weight:500;font-size:13px;color:#fff;text-transform:uppercase;margin-bottom:10px;letter-spacing:.4px}
.fcol .big{font-size:18px;font-weight:700;color:#fff}
.sub-row{display:flex;margin-top:14px}
.sub-row .input{width:190px;height:32px;background:#fff;color:var(--muted);font-size:11px;padding:0 10px;display:flex;align-items:center}
.sub-row .go{background:var(--orange);color:#fff;font-family:"Oswald",Arial,sans-serif;font-size:12px;text-transform:uppercase;padding:0 12px;display:flex;align-items:center}
</style>
</head>
<body>

<header class="hero">
  <div class="hero-photo" role="img" aria-label="Photo of a smiling repair engineer at the wheel of the service van"></div>
  <nav class="nav">
    <div class="brand"><span class="brand-dot"></span>Gadget Haven</div>
    <div class="nav-links">
      <span>Home</span><span>About Us</span><span>Services</span><span>Contact Us</span>
      <span class="btn">Request Order Flow</span>
    </div>
  </nav>
  <div class="hero-copy">
    <div class="line1">Professional Service</div>
    <div class="line2">On Location.</div>
    <div class="tag">Don't ship to us we will come to you!</div>
  </div>
  <div class="dots"><i class="on"></i><i></i><i></i><i></i><i></i></div>
</header>

<section class="about">
  <div class="about-col left">
    <h2 class="heading">Who We Are</h2><span class="rule"></span>
    <p>We are a team of skilled engineers who fix phones on the spot. Our vans carry every tool and part we need, so your device is repaired while you wait. No shipping, no long delays, no guesswork. Just a quick, honest and friendly repair at a place that suits you.</p>
    <p>We started with smartphones and will soon add tablets. Our call center plans each visit with care, and our repair center backs every engineer on the road.</p>
  </div>
  <div class="about-col right">
    <h2 class="heading">What We Do</h2><span class="rule"></span>
    <p>We repair broken screens, tired batteries, water damage, cameras and sound issues, right at your home, office or any place you pick.</p>
    <ul class="ticks">
      <li><svg width="12" height="12" viewBox="0 0 12 12"><path d="M1 6l3 3 7-7" fill="none" stroke="#f26522" stroke-width="2"/></svg>Screen and glass replacement on site.</li>
      <li><svg width="12" height="12" viewBox="0 0 12 12"><path d="M1 6l3 3 7-7" fill="none" stroke="#f26522" stroke-width="2"/></svg>New batteries fitted while you wait.</li>
      <li><svg width="12" height="12" viewBox="0 0 12 12"><path d="M1 6l3 3 7-7" fill="none" stroke="#f26522" stroke-width="2"/></svg>Water damage checked and cleaned.</li>
      <li><svg width="12" height="12" viewBox="0 0 12 12"><path d="M1 6l3 3 7-7" fill="none" stroke="#f26522" stroke-width="2"/></svg>Camera, speaker and mic repairs.</li>
      <li><svg width="12" height="12" viewBox="0 0 12 12"><path d="M1 6l3 3 7-7" fill="none" stroke="#f26522" stroke-width="2"/></svg>Charging port and button fixes.</li>
    </ul>
  </div>
  <div class="collage" role="img" aria-label="Collage of hands repairing phone circuit boards with small tools"></div>
  <div class="van" role="img" aria-label="White Gadget Haven service van seen from the side"></div>
</section>

<section class="why">
  <h2 class="heading center">Why The Customer Should Choose Us</h2>
  <p class="why-lead">Professional service on location. Don't ship<br>to us we will come to you!</p>
  <div class="ring"></div>
  <div class="ring-photo" role="img" aria-label="Smiling engineer in blue work uniform holding a tablet"></div>

  <div class="ring-icon" style="left:568px;top:175px"><svg width="26" height="30" viewBox="0 0 26 30"><path d="M13 29s10-10 10-17A10 10 0 003 12c0 7 10 17 10 17z" fill="none" stroke="#fff" stroke-width="2.5"/><circle cx="13" cy="12" r="3.5" fill="#fff"/></svg></div>
  <div class="ring-icon" style="left:446px;top:228px"><svg width="30" height="24" viewBox="0 0 30 24"><rect x="2" y="3" width="26" height="18" rx="3" fill="none" stroke="#fff" stroke-width="2.5"/><rect x="18" y="9" width="10" height="6" fill="#fff"/></svg></div>
  <div class="ring-icon" style="left:393px;top:348px"><svg width="32" height="24" viewBox="0 0 32 24"><path d="M2 4h18v13H2zM20 9h6l4 4v4H20z" fill="none" stroke="#fff" stroke-width="2.5"/><circle cx="8" cy="19" r="3" fill="#fff"/><circle cx="25" cy="19" r="3" fill="#fff"/></svg></div>
  <div class="ring-icon" style="left:459px;top:480px"><svg width="26" height="30" viewBox="0 0 26 30"><circle cx="13" cy="11" r="8" fill="none" stroke="#fff" stroke-width="2.5"/><path d="M8 18l-3 10 8-4 8 4-3-10" fill="none" stroke="#fff" stroke-width="2.5"/></svg></div>
  <div class="ring-icon" style="left:690px;top:236px"><svg width="28" height="28" viewBox="0 0 28 28"><path d="M6 3l5 5-3 4c2 4 4 6 8 8l4-3 5 5-4 4C11 26 2 17 2 7z" fill="#fff"/></svg></div>
  <div class="ring-icon" style="left:738px;top:348px"><svg width="28" height="28" viewBox="0 0 28 28"><path d="M6 4l6 6-3 3M22 24l-10-10M20 3l5 5-9 9-5-5z" fill="none" stroke="#fff" stroke-width="2.5"/></svg></div>
  <div class="ring-icon" style="left:679px;top:480px"><svg width="28" height="28" viewBox="0 0 28 28"><path d="M14 2l10 4v8c0 6-5 10-10 12C9 24 4 20 4 14V6z" fill="none" stroke="#fff" stroke-width="2.5"/><path d="M9 14l4 4 6-7" fill="none" stroke="#fff" stroke-width="2.5"/></svg></div>

  <p class="usp l" style="left:208px;top:246px">Clear pricing upfront.<br>No hidden cost.</p>
  <p class="usp l" style="left:165px;top:372px">Next business-day repair.</p>
  <p class="usp l" style="left:225px;top:496px">Repair is done by certified<br>engineers</p>
  <p class="usp" style="left:768px;top:248px">Backed by a professional call center<br>open 12 hours a day and open on a<br>Saturday as well</p>
  <p class="usp" style="left:816px;top:356px">Backed by a professional repair<br>center with more than 12 years of<br>experience</p>
  <p class="usp" style="left:757px;top:496px">1 year warranty on<br>the repair</p>
</section>

<section class="process">
  <h2 class="heading center">The Process</h2><span class="rule" style="margin:10px auto 0"></span>
  <div class="steps">
    <div class="step">
      <div class="step-icon"><svg width="28" height="42" viewBox="0 0 28 42"><rect x="2" y="2" width="24" height="38" rx="4" fill="none" stroke="#666" stroke-width="2.5"/><circle cx="14" cy="34" r="2" fill="#666"/></svg></div>
      <p>Choose your device<br>and repair job</p>
      <svg class="step-arrow" width="22" height="12" viewBox="0 0 22 12"><path d="M0 6h20M15 1l5 5-5 5" fill="none" stroke="#bbb" stroke-width="2"/></svg>
    </div>
    <div class="step">
      <div class="step-icon"><svg width="40" height="36" viewBox="0 0 40 36"><path d="M2 4h6l5 20h20l4-14H11" fill="none" stroke="#666" stroke-width="2.5"/><circle cx="15" cy="31" r="3" fill="#666"/><circle cx="31" cy="31" r="3" fill="#666"/></svg></div>
      <p>Place the order</p>
      <svg class="step-arrow" width="22" height="12" viewBox="0 0 22 12"><path d="M0 6h20M15 1l5 5-5 5" fill="none" stroke="#bbb" stroke-width="2"/></svg>
    </div>
    <div class="step">
      <div class="step-icon"><svg width="40" height="40" viewBox="0 0 40 40"><circle cx="20" cy="20" r="17" fill="none" stroke="#666" stroke-width="2.5"/><path d="M14 11l4 4-2 3c1 3 3 5 6 6l3-2 4 4-3 3c-8 0-15-7-15-15z" fill="#666"/></svg></div>
      <p>Get a callback<br>within the hour</p>
      <svg class="step-arrow" width="22" height="12" viewBox="0 0 22 12"><path d="M0 6h20M15 1l5 5-5 5" fill="none" stroke="#bbb" stroke-width="2"/></svg>
    </div>
    <div class="step">
      <div class="step-icon"><svg width="40" height="40" viewBox="0 0 40 40"><rect x="3" y="6" width="30" height="28" rx="2" fill="none" stroke="#666" stroke-width="2.5"/><path d="M3 14h30M10 2v8M26 2v8" stroke="#666" stroke-width="2.5"/><circle cx="31" cy="31" r="7" fill="#fff" stroke="#666" stroke-width="2.5"/><path d="M31 28v4h3" stroke="#666" stroke-width="2" fill="none"/></svg></div>
      <p>Set date and<br>location</p>
      <svg class="step-arrow" width="22" height="12" viewBox="0 0 22 12"><path d="M0 6h20M15 1l5 5-5 5" fill="none" stroke="#bbb" stroke-width="2"/></svg>
    </div>
    <div class="step">
      <div class="step-icon"><svg width="44" height="32" viewBox="0 0 44 32"><path d="M2 6h24v18H2zM26 12h9l6 6v6H26z" fill="none" stroke="#666" stroke-width="2.5"/><circle cx="10" cy="26" r="4" fill="#fff" stroke="#666" stroke-width="2.5"/><circle cx="34" cy="26" r="4" fill="#fff" stroke="#666" stroke-width="2.5"/></svg></div>
      <p>We will come to you.</p>
    </div>
  </div>
</section>

<section class="request">
  <div class="request-art" role="img" aria-label="Illustration of a smartphone, circuit board and repair tools"></div>
  <svg class="request-notch" width="1200" height="40" viewBox="0 0 1200 40"><path d="M0 0h1200v6L600 38 0 6z" fill="#3a3b3d"/></svg>
  <h2 class="heading">A Repair Request</h2>
  <div class="form-row">
    <div class="field wide">What parts need to be repaired</div>
    <div class="field sel">Model <svg width="10" height="6" viewBox="0 0 10 6"><path d="M0 0h10L5 6z" fill="#f26522"/></svg></div>
    <div class="field sel" style="width:175px">Brand <svg width="10" height="6" viewBox="0 0 10 6"><path d="M0 0h10L5 6z" fill="#f26522"/></svg></div>
    <span class="radio"><i class="on"></i>He</span>
    <span class="radio"><i></i>She</span>
  </div>
  <span class="btn">Place the order</span>
</section>

<section class="reviews">
  <div role="img" aria-label="Mosaic of customer portrait photos in dark tones" style="position:absolute;inset:0"></div>
  <svg class="reviews-stripe" width="1200" height="40" viewBox="0 0 1200 40"><path d="M600 14L1200 0v14L600 28z" fill="#f26522"/><path d="M0 0h1200L600 14z" fill="#8db4cf"/></svg>
  <div class="quote">&ldquo;</div>
  <h2 class="heading">What Our Customers Say</h2>
  <span class="rule" style="position:absolute;top:122px;left:580px"></span>

  <div class="review" style="left:172px">Fast, friendly and right at my door. My cracked screen was like new in under an hour and the price was just what they said it would be. I will book them again.
    <div class="stars">★★★★★</div><b>Mark Olsen</b><small>Happy customer</small></div>
  <div class="review" style="left:467px">The engineer came to my office and fixed my battery while I worked. Clear, calm and very kind. No shipping and no waiting for weeks. A great service.
    <div class="stars">★★★★★</div><b>Lena Vries</b><small>Happy customer</small></div>
  <div class="review" style="left:762px">My phone fell in water and I feared the worst. They came the next day, cleaned it and it works again. Polite team, fair price and a year of warranty.
    <div class="stars">★★★★★</div><b>Paul Graaf</b><small>Happy customer</small></div>

  <span class="avatar-line" style="left:303px"></span><span class="avatar" role="img" aria-label="Portrait of reviewer" style="left:269px"></span>
  <span class="avatar-line" style="left:598px"></span><span class="avatar" role="img" aria-label="Portrait of reviewer" style="left:564px"></span>
  <span class="avatar-line" style="left:893px"></span><span class="avatar" role="img" aria-label="Portrait of reviewer" style="left:859px"></span>
</section>

<section class="corporate">
  <h2 class="heading center">We Provide For Corporate Clients</h2><span class="rule" style="margin:10px auto 0"></span>
  <div class="corp-card" style="left:172px">
    <div class="corp-img" role="img" aria-label="Businessman with glowing gear graphics" style="background:linear-gradient(135deg,#1f3140,#4b6b84)"></div>
    <h3>Fleet repairs for your whole team, planned on your schedule.</h3><span class="rule"></span>
    <p>One contact, one invoice and quick on site repairs for every phone your staff use each day.</p>
    <span class="btn">Read More</span>
  </div>
  <div class="corp-card" style="left:467px">
    <div class="corp-img" role="img" aria-label="Smiling call center agent with headset" style="background:linear-gradient(135deg,#e9e6e2,#9b8c80)"></div>
    <h3>A direct line to our call center for your business needs.</h3><span class="rule"></span>
    <p>Priority booking, clear rates and a team that knows your devices and your offices well.</p>
    <span class="btn">Read More</span>
  </div>
  <div class="corp-card" style="left:760px">
    <div class="corp-img" role="img" aria-label="Hand touching a screen of connected gear icons" style="background:linear-gradient(135deg,#2f5a78,#7aa3bd)"></div>
    <h3>Service plans that keep your company connected all year.</h3><span class="rule"></span>
    <p>Regular checks, spare parts ready and engineers on location within one working day.</p>
    <span class="btn">Read More</span>
  </div>
</section>

<footer class="footer">
  <svg class="footer-tab" width="100" height="28" viewBox="0 0 100 28"><path d="M0 0h100L80 28H20z" fill="#fff"/><path d="M50 20V8M44 13l6-6 6 6" fill="none" stroke="#3a3a3b" stroke-width="2"/></svg>
  <div class="brand"><span class="brand-dot"></span>Gadget Haven</div>
  <span class="btn">Request Order Flow</span>
  <p class="copy">© 2017 Gadget Haven</p>
  <div class="fcol" style="left:425px">
    <h4>Quick Links</h4>Home<br>About Us<br>Services<br>Contact Us
  </div>
  <div class="fcol" style="left:567px">
    <h4>Contact Us</h4>Gadget Haven<br>Harbour Street 12<br>City<br><br>Phone<br><span class="big">(100) 555-010</span><br><br>Email<br>info@gadgethaven.com
  </div>
  <div class="fcol" style="left:757px;width:280px">
    <h4>Newsletter Subscribe</h4>Enter your email address below and get the latest news and offers.
    <div class="sub-row"><span class="input">Enter your Email Id here...</span><span class="go">Subscribe</span></div>
  </div>
</footer>

</body>
</html>
```